buseisness card

design a card that similar to my web site
BRIXENTAPLORLLC .COM

Contact Information for Business Card

NAME PHONE # WEBSITE EMAIL AND DISCTIPTION OF WHAT WE DO

Colors
0054AA
0677BA
7BADD7
CADEEF
E8F1F8

Requirements
Must have
• lOGO AND DETAILS
Nice to have
• I LIKE THE WATER LIKE ON MY WEB SITE

```html
<!DOCTYPE html>
<html lang="en">
<head>
<meta charset="utf-8">
<title>Brixentaplor Business Card</title>
<link href="https://fonts.googleapis.com/css2?family=Open+Sans:wght@400;600;700&display=swap" rel="stylesheet">
<style>
  :root {
    --backdrop: #e8e5e0;
    --card: #ffffff;
    --brand-blue: #1d86c3;
    --text-grey: #555a5f;
    --icon-blue: #2d95d2;
    --band-deep: #0b4a74;
    --band-mid: #1c6a9a;
    --address: #9fd2f0;
  }
  * { margin: 0; padding: 0; box-sizing: border-box; }
  html, body {
    width: 1200px; height: 831px; overflow: hidden;
    background: var(--backdrop);
    font-family: "Open Sans", Arial, sans-serif;
  }
  .business-card {
    position: absolute; left: 75px; top: 121px;
    width: 1050px; height: 589px;
    background: var(--card);
    box-shadow: 0 6px 18px rgba(0,0,0,0.18);
    overflow: hidden;
  }
  .water-band {
    position: absolute; left: 0; bottom: 0;
    width: 100%; height: 110px;
    background: linear-gradient(180deg, var(--band-mid) 0%, var(--band-deep) 45%, var(--band-deep) 100%);
  }
  .brand { position: absolute; left: 75px; top: 78px; width: 278px; text-align: center; }
  .brand-dot {
    width: 92px; height: 92px; border-radius: 50%;
    background: var(--brand-blue); margin: 0 auto 12px;
  }
  .brand-name {
    font-weight: 700; font-size: 27px; color: var(--brand-blue); letter-spacing: 0.5px;
  }
  .person { position: absolute; right: 53px; top: 168px; text-align: right; color: var(--text-grey); }
  .person-name { font-size: 30px; font-weight: 400; letter-spacing: 1.5px; line-height: 36px; }
  .person-title { font-size: 17px; letter-spacing: 3.5px; line-height: 30px; }
  .contact-list { position: absolute; list-style: none; color: var(--text-grey); font-size: 27px; line-height: 37px; letter-spacing: 1px; }
  .contact-list li { display: flex; align-items: center; gap: 14px; }
  .contact-list svg { width: 22px; height: 22px; fill: var(--icon-blue); flex: none; }
  .phones { left: 56px; top: 343px; }
  .online { right: 48px; top: 343px; }
  .online li { justify-content: flex-end; }
  .address {
    position: absolute; left: 56px; top: 533px;
    display: flex; align-items: center; gap: 14px;
    color: var(--address); font-size: 26px; letter-spacing: 1px;
  }
  .address svg { width: 22px; height: 28px; fill: var(--address); }
</style>
</head>
<body>
  <div class="business-card">
    <div class="water-band" role="img" aria-label="Blue water wave band along the bottom of the card"></div>

    <div class="brand">
      <div class="brand-dot"></div>
      <div class="brand-name">BRIXENTAPLOR</div>
    </div>

    <div class="person">
      <div class="person-name">PERSONS NAME</div>
      <div class="person-title">PERSONS TITLE</div>
    </div>

    <ul class="contact-list phones">
      <li><svg viewBox="0 0 24 24"><path d="M6.6 10.8a15.1 15.1 0 0 0 6.6 6.6l2.2-2.2c.3-.3.7-.4 1-.2 1.1.4 2.3.6 3.6.6.6 0 1 .4 1 1V20c0 .6-.4 1-1 1A17 17 0 0 1 3 4c0-.6.4-1 1-1h3.5c.6 0 1 .4 1 1 0 1.3.2 2.5.6 3.6.1.3 0 .7-.2 1z"/></svg>(999) 222-5555</li>
      <li><svg viewBox="0 0 24 24"><path d="M7 1h10a2 2 0 0 1 2 2v18a2 2 0 0 1-2 2H7a2 2 0 0 1-2-2V3a2 2 0 0 1 2-2zm0 3v14h10V4zm5 15.5a1.2 1.2 0 1 0 0 2.4 1.2 1.2 0 0 0 0-2.4z"/></svg>(999) 222-4444</li>
    </ul>

    <ul class="contact-list online">
      <li>aaaaaa@nnn.com<svg viewBox="0 0 24 24"><path d="M2 5h20v14H2zm2 2v.5l8 5 8-5V7zm0 2.9V17h16V9.9l-8 5z"/></svg></li>
      <li>www.sssssss.com<svg viewBox="0 0 24 24"><path d="M12 2a10 10 0 1 0 0 20 10 10 0 0 0 0-20zm6.9 6h-3a15 15 0 0 0-1.3-3.9A8 8 0 0 1 18.9 8zM12 4c.9 1.2 1.6 2.5 2 4h-4c.4-1.5 1.1-2.8 2-4zM4.3 14a8 8 0 0 1 0-4h3.4a16 16 0 0 0 0 4zm.8 2h3a15 15 0 0 0 1.3 3.9A8 8 0 0 1 5.1 16zm3-8h-3a8 8 0 0 1 4.3-3.9C8.8 5.3 8.4 6.6 8.1 8zM12 20c-.9-1.2-1.6-2.5-2-4h4c-.4 1.5-1.1 2.8-2 4zm2.3-6H9.7a14 14 0 0 1 0-4h4.6a14 14 0 0 1 0 4zm.3 5.9c.6-1.2 1-2.5 1.3-3.9h3a8 8 0 0 1-4.3 3.9zm1.7-5.9a16 16 0 0 0 0-4h3.4a8 8 0 0 1 0 4z"/></svg></li>
    </ul>

    <div class="address">
      <svg viewBox="0 0 24 30"><path d="M12 0a11 11 0 0 0-11 11c0 8 11 19 11 19s11-11 11-19A11 11 0 0 0 12 0zm0 15.5a4.5 4.5 0 1 1 0-9 4.5 4.5 0 0 1 0 9z"/></svg>
      City, State Name, 777 Street Name str.
    </div>
  </div>
</body>
</html>
```